Webdesign für Lösungsanbieter für die Digitalisierung von Unternehmen
Zielgruppe
Wir sehen uns als Ihr Lösungsanbieter für die Digitalisierung Ihres Unternehmens. Durch unser breit aufgestelltes Leistungsportfolio sind wird in der Lage Sie mit Komplettlösungen im Bereich Bürokommunikation und Infrastruktur zu unterstützen.
Wir wünschen uns ein neues frisches Design, gerne etwas unkonventionell. Unsere Zielgruppe sind kleine bis Mittelständige Unternehmen. Labore sind die Zielgruppe für unsere eigenen Produkte. Des weiteren betreuen wir deutschlandweit Kunden im Cloudbereich und IP Telefonie.
Unsere Tätigkeit
- IT Systemhaus (Verkauf und Installation von IT Systemem)
- Softwareentwicklung (eingene Produkte sowie Auftragsentwicklungen für Kunden)
- IP Telefonsysteme
- Sicherheitstechnik
- Clouddiesnste (Rechnenzentrum, SaaS,IAAS)
- Webhosting
- Consulting
- Netzwerktechnik (Glasfaser und Kupfer).
Aufgabenstellung
Wir bitten um offene Daten.

```html
<!DOCTYPE html>
<html lang="de">
<head>
<meta charset="utf-8">
<title>Novaris – IT Solutions</title>
<link href="https://fonts.googleapis.com/css2?family=Oswald:wght@500;600&family=Roboto:wght@300;400;500;700&family=Roboto+Condensed:wght@300;400&display=swap" rel="stylesheet">
<style>
:root{
  --navy:#15142b;
  --navy-2:#1c1b38;
  --orange:#e8841d;
  --green:#b8c241;
  --text:#222;
  --muted:#555;
  --light:#f0f0f0;
  --line:#dcdcdc;
  --white:#fff;
}
*{box-sizing:border-box;margin:0;padding:0}
html,body{width:1200px;height:3721px;overflow:hidden}
body{font-family:"Roboto",sans-serif;color:var(--text);background:var(--white);position:relative}
.wrap{position:relative}
/* brand */
.brand{display:flex;align-items:center;gap:12px;font-family:"Roboto",sans-serif;font-weight:300;color:var(--white);font-size:46px;letter-spacing:1px}
.brand-dot{width:46px;height:46px;border-radius:50%;background:var(--orange)}
/* hero */
.hero{height:440px;background:var(--navy);position:relative;overflow:hidden}
.hero-visual{position:absolute;left:520px;top:0;width:680px;height:400px;background:radial-gradient(ellipse at 55% 50%,#2e6fa3 0%,#1b3a64 35%,var(--navy) 75%)}
.nav{position:absolute;top:48px;left:173px;right:175px;display:flex;align-items:center;justify-content:space-between}
.nav ul{display:flex;list-style:none;gap:24px;align-items:center;font-size:11px;color:var(--white)}
.nav ul li.active{color:var(--orange)}
.nav .btn-contact{background:var(--orange);padding:9px 16px;color:var(--white)}
.hero-label{position:absolute;left:175px;top:139px;font-size:10px;color:var(--green);text-transform:uppercase}
.hero h1{position:absolute;left:172px;top:152px;font-family:"Oswald",sans-serif;font-weight:600;font-size:46px;line-height:51px;color:var(--white);text-transform:uppercase}
.hero p{position:absolute;left:175px;top:322px;width:280px;font-size:12px;line-height:17px;color:#d7d7e3}
.hero-wave{position:absolute;left:0;bottom:0;width:1200px;height:90px}
/* heading block */
.sec-head{text-align:center}
.sec-icon{width:46px;height:32px;border-radius:50%;background:var(--orange);margin:0 auto 14px}
.sec-label{font-size:12px;color:var(--orange);text-transform:uppercase}
.sec-title{font-size:19px;font-weight:700;color:var(--text);text-transform:uppercase;margin-top:8px}
/* services */
.services{padding-top:60px;height:831px}
.grid{width:850px;margin:50px auto 0;display:grid;grid-template-columns:repeat(4,207px);gap:15px 7px}
.card{border:1px solid var(--line);height:266px;text-align:center}
.card-img{height:115px}
.card h3{font-size:11px;font-weight:500;margin:20px 0 10px;text-transform:uppercase}
.card p{font-size:9px;line-height:12px;color:var(--muted);padding:0 20px}
.card .more{display:inline-block;margin-top:18px;border:1px solid var(--orange);color:var(--orange);font-size:8px;padding:7px 14px}
/* cta */
.cta{height:159px;background:var(--navy);border-top:5px solid var(--orange);text-align:center;color:var(--white);padding-top:24px;position:relative}
.cta::before{content:"";position:absolute;right:0;top:-5px;width:400px;height:5px;background:var(--green)}
.cta h2{font-family:"Roboto Condensed",sans-serif;font-weight:400;font-size:30px}
.cta .sub{font-size:11px;margin-top:2px;color:#ddd}
.cta-row{display:flex;justify-content:center;align-items:center;gap:18px;margin-top:16px}
.cta-phone{font-family:"Roboto Condensed",sans-serif;font-weight:300;font-size:22px;color:var(--green);padding-right:18px;border-right:2px solid var(--white)}
.btn{display:inline-flex;align-items:center;gap:6px;background:var(--orange);color:var(--white);border-radius:20px;font-size:9px;padding:10px 18px;text-transform:uppercase}
/* about */
.about{height:323px;background:var(--light);position:relative;overflow:hidden}
.about-deco{position:absolute;left:-60px;top:10px;width:320px;height:300px;border-radius:50%;background:#e2e2e2}
.about-left{position:absolute;left:175px;top:107px;width:280px}
.about-left .label{font-size:12px;color:var(--orange);text-transform:uppercase}
.about-left h2{font-size:18px;font-weight:700;line-height:25px;margin-top:10px;text-transform:uppercase}
.about-divider{position:absolute;left:470px;top:100px;width:1px;height:110px;background:var(--line)}
.about-right{position:absolute;left:502px;top:96px;width:510px}
.about-right h3{font-size:12px;font-weight:500}
.about-right p{font-size:10px;line-height:14px;color:var(--muted);margin:20px 0 22px}
.about-right .btn{text-transform:none;font-size:10px}
/* why */
.why{height:530px;display:flex;background:var(--navy);position:relative}
.why-img{width:592px;height:530px;background:linear-gradient(135deg,#9a9ea5,#5a4e4a 60%,#3a3640)}
.why-badge{position:absolute;left:545px;top:205px;width:100px;height:100px;border-radius:50%;background:var(--navy);border:3px solid #2c2b4a}
.why-badge span{position:absolute;left:25px;top:28px;width:50px;height:40px;border-radius:50%;background:var(--orange)}
.why-body{padding:76px 0 0 64px;color:var(--white);width:420px}
.why-body .label{font-size:12px;color:var(--green);text-transform:uppercase}
.why-body h2{font-size:23px;font-weight:500;line-height:34px;margin-top:8px;text-transform:uppercase}
.why-body p{font-size:10px;line-height:14px;margin-top:18px;color:#ddd}
.feature{display:flex;gap:14px;margin-top:26px}
.feature svg{flex:0 0 26px}
.feature h4{font-size:12px;font-weight:400;color:var(--orange)}
.feature div p{margin-top:6px;font-size:9px;font-weight:500;color:var(--white)}
/* news */
.news{height:658px;padding-top:92px}
.news-grid{display:flex;gap:22px;justify-content:center;margin-top:50px}
.post{width:224px;height:354px;background:#eee;border-radius:8px;overflow:hidden;position:relative}
.post-img{height:140px}
.post-date{position:absolute;left:166px;top:116px;width:42px;height:40px;background:var(--orange);color:var(--white);font-size:9px;text-align:center;padding-top:7px;line-height:11px}
.post-body{padding:20px 18px}
.post-cat{font-size:9px;color:var(--orange)}
.post h3{font-size:13px;font-weight:400;line-height:16px;margin-top:12px}
.post p{font-size:9px;line-height:13px;color:var(--muted);margin-top:12px}
.post .arrow{display:inline-block;margin-top:20px;background:var(--orange);color:var(--white);border-radius:15px;width:42px;height:26px;text-align:center;line-height:26px;font-size:12px}
/* contact */
.contact{height:452px;background:#f4f4f4;position:relative;overflow:hidden}
.contact-box{position:absolute;left:258px;top:65px;width:223px;height:337px;background:var(--orange);box-shadow:12px 12px 0 var(--green);color:var(--white);padding:46px 16px 0}
.c-item{display:flex;gap:12px;padding-bottom:22px;margin-bottom:26px;border-bottom:1px solid rgba(255,255,255,.35)}
.c-item:last-child{border:none}
.c-item h4{font-size:16px;font-weight:400}
.c-item p{font-size:9px;line-height:11px;margin-top:3px}
.contact-form{position:absolute;left:538px;top:82px;width:412px}
.contact-form .label{font-size:12px;color:var(--orange);text-transform:uppercase}
.contact-form h2{font-size:16px;font-weight:700;margin-top:6px;text-transform:uppercase}
.field{border-bottom:1px solid #bbb;font-size:9px;color:var(--orange);padding-bottom:12px;margin-top:26px}
.row{display:flex;gap:38px}.row .field{flex:1}
.field.tall{height:100px}
.contact-form .btn{margin-top:40px;text-transform:none;font-size:10px}
/* footer */
.footer{height:350px;background:var(--navy);position:relative;color:var(--white);text-align:center}
.footer-wave{position:absolute;left:0;top:-66px;width:1200px;height:112px}
.footer ul{list-style:none;display:flex;justify-content:center;gap:24px;font-size:11px;padding-top:132px}
.footer .copy{font-size:10px;margin-top:16px}
.footer .brand{justify-content:center;margin-top:32px;font-size:50px}
</style>
</head>
<body>
<header class="hero">
  <div class="hero-visual" role="img" aria-label="Leuchtendes Netzwerk über der Erde bei Nacht"></div>
  <nav class="nav">
    <div class="brand"><span class="brand-dot"></span>novaris</div>
    <ul>
      <li class="active">STARTSEITE</li><li>DIENSTLEISTUNGEN</li><li>PREIS</li><li>ÜBER UNS</li><li>BLOG</li><li class="btn-contact">KONTAKT</li>
    </ul>
  </nav>
  <div class="hero-label">Wir sind ein führendes Technologieunternehmen</div>
  <h1>Integrierte Lösung<br>für das digitale<br>Zeitalter</h1>
  <p>Orem ipsum dolor sit amet, consectetur adipiscing elit utelit tellus, luctus nec ullam corper mattis, pulvinar dapibus leo nulla metus.</p>
  <svg class="hero-wave" viewBox="0 0 1200 90" preserveAspectRatio="none">
    <path d="M0 50 C300 100 700 30 1200 0 L1200 90 L0 90Z" fill="var(--orange)"/>
    <path d="M0 30 C200 70 500 80 700 62 L700 90 L0 90Z" fill="var(--green)"/>
    <path d="M0 62 C300 100 700 40 1200 22 L1200 90 L0 90Z" fill="#fff"/>
  </svg>
</header>

<section class="services">
  <div class="sec-head">
    <div class="sec-icon"></div>
    <div class="sec-label">Wir bieten ein breites</div>
    <h2 class="sec-title">Vielzahl von Digitalisierungslösungen</h2>
  </div>
  <div class="grid">
    <article class="card"><div class="card-img" role="img" aria-label="Techniker verkabelt einen Server" style="background:linear-gradient(135deg,#d8d8d8,#6b6b6b)"></div><h3>IT Systemhaus</h3><p>Lorem ipsum dolor sit amet, consectetur adipiscing elit. Ut elit tellus, luctus nec ullamcorper mattis, pulvinar dapibus leo.</p><span class="more">Weiterlesen</span></article>
    <article class="card"><div class="card-img" role="img" aria-label="Hände mit Software-Symbolen" style="background:linear-gradient(135deg,#3a2a2a,#e08a40)"></div><h3>Softwareentwicklung</h3><p>Lorem ipsum dolor sit amet, consectetur adipiscing elit. Ut elit tellus, luctus nec ullamcorper mattis, pulvinar dapibus leo.</p><span class="more">Weiterlesen</span></article>
    <article class="card"><div class="card-img" role="img" aria-label="IP-Telefon vor Serverschrank" style="background:linear-gradient(135deg,#3b4a6a,#1a1f2e)"></div><h3>IP Telefonsysteme</h3><p>Lorem ipsum dolor sit amet, consectetur adipiscing elit. Ut elit tellus, luctus nec ullamcorper mattis, pulvinar dapibus leo.</p><span class="more">Weiterlesen</span></article>
    <article class="card"><div class="card-img" role="img" aria-label="Digitales Sicherheitsschild über Stadt" style="background:linear-gradient(135deg,#1a3f8a,#3d7fd0)"></div><h3>Sicherheitstechnik</h3><p>Lorem ipsum dolor sit amet, consectetur adipiscing elit. Ut elit tellus, luctus nec ullamcorper mattis, pulvinar dapibus leo.</p><span class="more">Weiterlesen</span></article>
    <article class="card"><div class="card-img" role="img" aria-label="Laptop mit Cloud-Symbol" style="background:linear-gradient(135deg,#6a5030,#2a2420)"></div><h3>Clouddiesnste</h3><p>Lorem ipsum dolor sit amet, consectetur adipiscing elit. Ut elit tellus, luctus nec ullamcorper mattis, pulvinar dapibus leo.</p><span class="more">Weiterlesen</span></article>
    <article class="card"><div class="card-img" role="img" aria-label="Serverreihen im Rechenzentrum" style="background:linear-gradient(135deg,#9a9a9a,#2e2e2e)"></div><h3>Webhosting</h3><p>Lorem ipsum dolor sit amet, consectetur adipiscing elit. Ut elit tellus, luctus nec ullamcorper mattis, pulvinar dapibus leo.</p><span class="more">Weiterlesen</span></article>
    <article class="card"><div class="card-img" role="img" aria-label="Beratungsgespräch mit Dokumenten" style="background:linear-gradient(135deg,#d9dde3,#7a8da3)"></div><h3>Consulting</h3><p>Lorem ipsum dolor sit amet, consectetur adipiscing elit. Ut elit tellus, luctus nec ullamcorper mattis, pulvinar dapibus leo.</p><span class="more">Weiterlesen</span></article>
    <article class="card"><div class="card-img" role="img" aria-label="Leuchtendes Glasfaserkabel" style="background:linear-gradient(90deg,#1a2540,#e8601d 70%,#f5c060)"></div><h3>Netzwerktechnik</h3><p>Lorem ipsum dolor sit amet, consectetur adipiscing elit. Ut elit tellus, luctus nec ullamcorper mattis, pulvinar dapibus leo.</p><span class="more">Weiterlesen</span></article>
  </div>
</section>

<section class="cta">
  <h2>KOSTENLOSE ERSTBERATUNG</h2>
  <div class="sub">Jetzt Termin vereinbaren und 30 Minuten kostenlose Beratung erhalten.</div>
  <div class="cta-row"><span class="cta-phone">+49 68 00 | 123 45-0</span><span class="btn">Planen Sie Ihr Meeting</span></div>
</section>

<section class="about">
  <div class="about-deco"></div>
  <div class="about-left">
    <div class="label">Über unsere Firma</div>
    <h2>Wir helfen Unternehmen, im digitalen Zeitalter voranzukommen</h2>
  </div>
  <div class="about-divider"></div>
  <div class="about-right">
    <h3>Dies ist die Hauptüberschrift</h3>
    <p>Lorem ipsum dolor sit amet, consectetur adipiscing elit, sed do eiusmod tempor incididunt ut labore et dolore magna aliqua. Ut enim ad minim veniam, quis nostrud exercitation ullamco laboris nisi ut aliquip ex ea commodo consequat.</p>
    <span class="btn">View All →</span>
  </div>
</section>

<section class="why">
  <div class="why-img" role="img" aria-label="Team im Besprechungsraum"></div>
  <div class="why-badge"><span></span></div>
  <div class="why-body">
    <div class="label">Warum uns wählen</div>
    <h2>Seit über 30 Jahren in der Technologiebranche</h2>
    <p>Lorem ipsum dolor sit amet, consectetur adipiscing elit, sed do eiusmod tempor incididunt ut labore et dolore magna aliqua. Ut enim ad minim veniam, quis nostrud exercitation ullamco laboris nisi ut aliquip ex ea commodo consequat.</p>
    <div class="feature"><svg width="26" height="26" viewBox="0 0 26 26" fill="none" stroke="var(--orange)" stroke-width="1.5"><circle cx="13" cy="13" r="11"/><circle cx="13" cy="13" r="5"/></svg><div><h4>Experten für technischen Support</h4><p>Diam vel quam elementum pulvinar ac tium aenean pharetra magna ac placerat quis eget.</p></div></div>
    <div class="feature"><svg width="26" height="26" viewBox="0 0 26 26" fill="none" stroke="var(--orange)" stroke-width="1.5"><path d="M13 2l3.3 7 7.5.9-5.6 5.1 1.5 7.5L13 18.8 6.3 22.5l1.5-7.5L2.2 9.9l7.5-.9z"/></svg><div><h4>Solide Teamarbeit</h4><p>Diam vel quam elementum pulvinar ac tium aenean pharetra magna ac placerat quis eget.</p></div></div>
    <div class="feature"><svg width="26" height="26" viewBox="0 0 26 26" fill="none" stroke="var(--orange)" stroke-width="1.5"><rect x="2" y="3" width="22" height="20"/><path d="M6 9h14M6 14h10M6 19h7"/></svg><div><h4>Fortschrittliche Technologie</h4><p>Diam vel quam elementum pulvinar ac tium aenean pharetra magna ac placerat quis eget.</p></div></div>
  </div>
</section>

<section class="news">
  <div class="sec-head">
    <div class="sec-icon"></div>
    <div class="sec-label">Bleiben Sie mit Novaris auf dem Laufenden</div>
    <h2 class="sec-title">Von den neuesten &amp; beliebten News</h2>
  </div>
  <div class="news-grid">
    <article class="post"><div class="post-img" role="img" aria-label="Industriemaschine in Nahaufnahme" style="background:linear-gradient(135deg,#a0a4a8,#2e3238)"></div><div class="post-date">July 19<br>2021</div><div class="post-body"><div class="post-cat">▭ Artificial Store</div><h3>Repeated of endeavor mr position kindness.</h3><p>Lorem ipsum dolor sit amet, consectetur adipiscing elit, sed do eiusmod tempor incididunt ut labore.</p><span class="arrow">→</span></div></article>
    <article class="post"><div class="post-img" role="img" aria-label="Techniker an einer Produktionsanlage" style="background:linear-gradient(135deg,#6a7a90,#c0583a)"></div><div class="post-date">July 19<br>2021</div><div class="post-body"><div class="post-cat">▭ Automation</div><h3>Justifying Automation in Your Factory.</h3><p>Lorem ipsum dolor sit amet, consectetur adipiscing elit, sed do eiusmod tempor incididunt ut labore.</p><span class="arrow">→</span></div></article>
    <article class="post"><div class="post-img" role="img" aria-label="Roboterarm in einer Fertigungshalle" style="background:linear-gradient(135deg,#b0b4b8,#4a4e54)"></div><div class="post-date">July 19<br>2021</div><div class="post-body"><div class="post-cat">▭ Digitalization</div><h3>Boost Your Cobot Safety Know-How with These Digital Resources</h3><p>Lorem ipsum dolor sit amet, consectetur adipiscing elit, sed do eiusmod tempor incididunt ut labore.</p><span class="arrow">→</span></div></article>
  </div>
</section>

<section class="contact">
  <div class="contact-box">
    <div class="c-item"><svg width="24" height="24" viewBox="0 0 24 24" fill="#fff"><path d="M12 2a7 7 0 0 0-7 7c0 5 7 13 7 13s7-8 7-13a7 7 0 0 0-7-7zm0 9.5A2.5 2.5 0 1 1 12 6.5a2.5 2.5 0 0 1 0 5z"/></svg><div><h4>Novaris GmbH</h4><p>Lindenweg 12<br>66111 Beispielstadt</p></div></div>
    <div class="c-item"><svg width="24" height="24" viewBox="0 0 24 24" fill="#fff"><path d="M6.6 10.8a15 15 0 0 0 6.6 6.6l2.2-2.2a1 1 0 0 1 1-.25 11.4 11.4 0 0 0 3.6.57 1 1 0 0 1 1 1V20a1 1 0 0 1-1 1A17 17 0 0 1 3 4a1 1 0 0 1 1-1h3.5a1 1 0 0 1 1 1c0 1.25.2 2.45.57 3.57a1 1 0 0 1-.25 1z"/></svg><div><h4>Einen Anruf tätigen</h4><p>+49 68 00 | 123 45-0</p></div></div>
    <div class="c-item"><svg width="24" height="24" viewBox="0 0 24 24" fill="#fff"><path d="M3 6h18v12H3z" fill="none" stroke="#fff" stroke-width="2"/><path d="M3 6l9 7 9-7" fill="none" stroke="#fff" stroke-width="2"/></svg><div><h4>Senden Sie eine E-Mail</h4><p>vertrieb@novaris.de</p></div></div>
  </div>
  <div class="contact-form">
    <div class="label">Wir freuen uns jederzeit von Ihnen zu hören</div>
    <h2>Machen Sie sich bereit, Ihr Projekt mit uns zu starten</h2>
    <div class="field">Name</div>
    <div class="row"><div class="field">Email*</div><div class="field">Phone</div></div>
    <div class="field tall">Tell Us About Project*</div>
    <span class="btn">Send Message ➤</span>
  </div>
</section>

<footer class="footer">
  <svg class="footer-wave" viewBox="0 0 1200 112" preserveAspectRatio="none">
    <path d="M0 70 C400 30 800 60 1200 0 L1200 112 L0 112Z" fill="var(--orange)"/>
    <path d="M0 62 C300 85 500 100 700 90 L700 112 L0 112Z" fill="var(--green)"/>
    <path d="M0 80 C400 110 800 40 1200 22 L1200 112 L0 112Z" fill="var(--navy)"/>
  </svg>
  <ul><li>STARTSEITE</li><li>DIENSTLEISTUNGEN</li><li>PREIS</li><li>ÜBER UNS</li><li>BLOG</li><li>KONTAKT</li></ul>
  <div class="copy">COPYRIGHT © 2021. ALL RIGHTS RESERVED.</div>
  <div class="brand"><span class="brand-dot"></span>novaris</div>
</footer>
</body>
</html>
```